Lustra Vale Label

Design a label for the new brand Lustra Vale. The specific product label : Lustra Vale Deep Moisturizing Conditioner.

You only need to design the front label.I have included the logo and a bottle jpeg. Please try your best.

Industry/Entity Type

Product

Requirements
Must have
• text you can use:
• For Dry, Damaged Hair
• Strengthening & Moisturizing Conditioner
• Moisture Infused
• Deep Penetrating Formula
• Used by Professionals
• 8.5oz/250ml

```html
<!DOCTYPE html>
<html lang="en">
<head>
<meta charset="utf-8">
<title>Lustra Vale Deep Moisturizing Conditioner – Front Label</title>
<link rel="stylesheet" href="https://fonts.googleapis.com/css2?family=Arimo:wght@400;700&family=Oswald:wght@500;600;700&display=swap">
<style>
  :root {
    --brown: #7a4a1f;
    --brown-text: #6b3f16;
    --yellow: #f7de0c;
    --yellow-deep: #f1c400;
    --white: #ffffff;
    --outline: #8a8a8a;
    --ink: #1a1a1a;
    --photo-dark: #3a3330;
    --photo-mid: #7b6a5e;
    --photo-light: #c9c6c4;
  }
  html, body {
    margin: 0;
    padding: 0;
    width: 1200px;
    height: 1200px;
    overflow: hidden;
    background: var(--white);
  }
  .sheet { display: block; width: 1200px; height: 1200px; }
  .label-body { fill: var(--white); stroke: var(--outline); stroke-width: 0.6; }
  .label-top { fill: var(--brown); }
  .foil { fill: var(--yellow); }
  .new-tag { font-family: "Arimo", Arial, sans-serif; font-weight: 700; font-style: italic; font-size: 9px; fill: var(--ink); }
  .brand-name { font-family: "Arimo", Arial, sans-serif; font-weight: 700; font-size: 21px; fill: var(--yellow); }
  .brand-mark { fill: var(--yellow); }
  .product-title { font-family: "Oswald", "Arial Narrow", sans-serif; font-weight: 700; font-size: 17px; fill: var(--brown-text); }
  .product-type { font-family: "Oswald", "Arial Narrow", sans-serif; font-weight: 600; font-size: 8px; fill: var(--brown-text); }
  .photo-ring { fill: none; stroke: var(--yellow); stroke-width: 3; }
  .photo-swoosh { fill: none; stroke: var(--yellow-deep); stroke-width: 2.2; stroke-linecap: round; }
  .benefit { font-family: "Oswald", "Arial Narrow", sans-serif; font-weight: 500; font-size: 8.2px; fill: var(--yellow-deep); letter-spacing: 0.2px; }
  .net-volume { font-family: "Arimo", Arial, sans-serif; font-size: 5px; fill: var(--yellow-deep); }
  .note-text { font-family: "Arimo", Arial, sans-serif; font-size: 26px; fill: var(--ink); }
  .note-line { stroke: var(--ink); stroke-width: 1.3; fill: none; }
  .note-arrow { fill: var(--ink); }
</style>
</head>
<body>
<svg class="sheet" viewBox="0 0 1200 1200" xmlns="http://www.w3.org/2000/svg">
  <defs>
    <radialGradient id="photoTone" cx="40%" cy="45%" r="70%">
      <stop offset="0%" stop-color="var(--photo-light)"/>
      <stop offset="55%" stop-color="var(--photo-mid)"/>
      <stop offset="100%" stop-color="var(--photo-dark)"/>
    </radialGradient>
    <clipPath id="archClip">
      <path d="M0 97.5 A97.5 97.5 0 0 1 195 97.5 V540 Q195 547 188 547 H7 Q0 547 0 540 Z"/>
    </clipPath>
    <marker id="arrowHead" viewBox="0 0 10 10" refX="9" refY="5" markerWidth="9" markerHeight="9" orient="auto">
      <path class="note-arrow" d="M0 1 L10 5 L0 9 Z"/>
    </marker>
  </defs>

  <!-- Front label -->
  <g class="front-label" transform="translate(520 60) scale(1.8)">
    <path class="label-body" d="M0 97.5 A97.5 97.5 0 0 1 195 97.5 V540 Q195 547 188 547 H7 Q0 547 0 540 Z"/>
    <g clip-path="url(#archClip)">
      <rect class="label-top" x="0" y="0" width="195" height="250"/>
      <rect class="foil new-band" x="0" y="9" width="195" height="18"/>
      <rect class="foil title-band" x="0" y="250" width="195" height="27"/>
    </g>
    <text class="new-tag" x="97.5" y="22" text-anchor="middle">NEW</text>

    <g class="brand">
      <circle class="brand-mark" cx="34" cy="152" r="6"/>
      <text class="brand-name" x="104" y="160" text-anchor="middle">Lustra Vale</text>
    </g>

    <text class="product-title" x="97.5" y="270.5" text-anchor="middle">DEEP MOISTURIZING</text>
    <text class="product-type" x="190" y="294" text-anchor="end">CONDITIONER</text>

    <g class="hero-photo">
      <circle cx="97" cy="377" r="58" fill="url(#photoTone)" role="img" aria-label="Portrait of a model with long flowing brown hair"/>
      <circle class="photo-ring" cx="97" cy="377" r="60"/>
      <path class="photo-swoosh" d="M38 392 A60 66 0 0 0 160 396"/>
    </g>

    <text class="benefit" x="97.5" y="480" text-anchor="middle">DEEP MOISTURIZING</text>
    <text class="benefit" x="97.5" y="497" text-anchor="middle">SOFTNESS AND SHINE</text>
    <text class="net-volume" x="97.5" y="535" text-anchor="middle">8.5oz/250ml</text>
  </g>

  <!-- Print notes -->
  <g class="foil-callout">
    <text class="note-text" x="312" y="740">Foiling</text>
    <text class="note-text" x="322" y="772">Area</text>
    <line class="note-line" x1="402" y1="760" x2="518" y2="534" marker-end="url(#arrowHead)"/>
    <line class="note-line" x1="402" y1="760" x2="574" y2="780" marker-end="url(#arrowHead)"/>
    <line class="note-line" x1="402" y1="760" x2="601" y2="846" marker-end="url(#arrowHead)"/>
  </g>

  <g class="colour-legend">
    <rect class="foil" x="330" y="1108" width="20" height="20"/>
    <text class="note-text" x="364" y="1127">Pantone 209 C &amp; Foiling Area</text>
  </g>
</svg>
</body>
</html>
```